Powerpoint visual improvements

I need a cover page, and our beliefs page and differentiating factors page / graphic design for our presentation. For the cover page I would just like an attractive design that incorporate our architectural concept with columns and potentially our logo. For the beliefs page I just want a more attractive presentatoin of the concepts. For the differentiating factors page I want a graphic that captures the points about how we are different from competitors. I have used the attached content to date, but I think it can be improved. The text is included in the graphic and I would also like to make sure the firm logo is incorporated.

Target Market(s)

Individual and institutional investors.

Industry/Entity Type

Investment Advisory

Requirements
Must have
• Our corporate colors are generally RGB 145,148,149; 66,68,76; 0,0,153; and 0,63,127. Our logo is attached. Our primary font is Georgia. Our website is www.PelmarCW.com. The key pages are www.PelmarCW.com/beliefs and www.PelmarCW.com/value we are trying to capture in a presentation. We also need a new presentation cover. Use the website as a reference for the type of imagery we like.

```html
<!DOCTYPE html>
<html lang="en">
<head>
<meta charset="utf-8">
<title>Pelmar Capital Wealth – Presentation Slides</title>
<link rel="stylesheet" href="https://fonts.googleapis.com/css2?family=Open+Sans:wght@400;600;700&display=swap">
<style>
:root{
  --navy:#123f84;
  --navy-deep:#0c2f69;
  --blue:#1f7fd1;
  --ink:#333a44;
  --text:#5b6068;
  --grey:#919495;
  --band:#ececec;
  --rule:#cfd3d8;
  --board:#cccccc;
  --white:#ffffff;
}
*{box-sizing:border-box;margin:0;padding:0}
html,body{width:1200px;height:902px;overflow:hidden;background:var(--board)}
.board{position:relative;width:1200px;height:902px;background:var(--board);font-family:"Open Sans",Arial,sans-serif;color:var(--text)}
.slide{position:absolute;width:248px;height:140px;background:var(--white);overflow:hidden;box-shadow:0 1px 3px rgba(0,0,0,.18)}
.slide--navy{background:var(--navy)}
.abs{position:absolute}
.slide-title{position:absolute;left:0;top:7px;height:9px;border-left:3px solid var(--navy);padding-left:5px;font-size:5px;font-weight:700;line-height:9px;color:var(--ink);letter-spacing:.1px}
.slide-footer{position:absolute;left:12px;right:10px;bottom:8px;border-top:.5px solid var(--rule)}
.slide-footer-mark{position:absolute;left:4px;bottom:5px;width:5px;height:5px;border:.7px solid var(--grey);border-radius:50%}
.fine{font-size:2.5px;line-height:3.3px;color:var(--text)}
.fine--white{color:#e3e9f3}
.lead{font-size:3.1px;font-weight:700;color:var(--ink)}
.item-head{font-size:3.8px;font-weight:700;color:var(--navy);margin-bottom:2px}
.photo{position:absolute}
.photo--office{background:linear-gradient(135deg,#7e8791,#b9bec4 45%,#4b5560)}
.photo--city{background:linear-gradient(160deg,#2d4f7e,#6d8fbf 45%,#e8b27b 80%,#3b4f6d)}
.photo--finance{background:linear-gradient(135deg,#1c3a8a,#6a7fd0 50%,#f07a90)}
.icon-dot{position:absolute;width:9px;height:9px;border-radius:50%;background:var(--navy);display:flex;align-items:center;justify-content:center}
.icon-dot svg{width:5px;height:5px}

/* cover */
.cover-shade{position:absolute;inset:0;background:rgba(18,63,132,.78)}
.cover-brand{position:absolute;left:82px;top:52px;display:flex;align-items:center;gap:4px}
.cover-brand-mark{width:30px;height:30px;border-radius:50%;background:var(--white)}
.cover-brand-name{font-size:15px;font-weight:400;color:var(--white);line-height:1}
.cover-brand-sub{font-size:3.6px;color:var(--white);letter-spacing:.5px;margin-top:2px}

/* beliefs */
.beliefs-band{position:absolute;left:0;right:0;top:22px;height:100px;background:var(--band)}
.belief{position:absolute;width:80px}
.belief-icon{position:absolute;width:8px;height:8px}

/* difference */
.diff-cell{position:absolute;width:70px;height:42px;border-left:.8px solid var(--navy);padding-left:3px}

/* lorem boxes */
.lorem-box{position:absolute;width:48px;height:23px;border:.6px solid var(--navy);padding-top:5px;text-align:center}
.lorem-box-tab{position:absolute;left:19px;top:-4px;width:10px;height:6px;background:var(--navy)}
.lorem-box-head{font-size:2.8px;font-weight:700;color:var(--ink)}

/* legend */
.legend{position:absolute;left:14px;display:flex;align-items:center;gap:4px;font-size:3px;font-weight:700;color:var(--ink)}
.legend-dot{width:6px;height:6px;border-radius:50%}

/* numbered list */
.num-row{position:absolute;left:6px;width:92px;height:13px;border-bottom:.5px solid #d6d6d6;display:flex;align-items:center;gap:4px}
.num-row b{font-size:5px;font-weight:400;color:var(--ink)}

/* labels */
.tag{position:absolute;top:84px;width:49px;height:6px;font-size:2.5px;color:var(--white);text-align:center;line-height:6px}

/* team */
.member{position:absolute;top:42px;width:40px;text-align:center}
.member-photo{width:32px;height:32px;margin:0 auto;border-radius:50%;background:radial-gradient(circle,#b7b9bc,#6f7276)}
.member-name{font-size:3.2px;font-weight:700;color:var(--navy);margin-top:3px}
.member-role{font-size:2.5px;color:var(--text)}

/* phone */
.phone-copy{position:absolute;width:50px}
.phone-copy b{display:block;font-size:2.8px;color:var(--navy)}

/* thank you */
.thanks{position:absolute;left:0;right:0;text-align:center;color:var(--white)}
</style>
</head>
<body>
<main class="board">

  <!-- Row 1 -->
  <section class="slide slide--navy" style="left:53px;top:47px">
    <div class="photo photo--office" style="inset:0" role="img" aria-label="Photo of colleagues meeting around a table"></div>
    <div class="cover-shade"></div>
    <div class="cover-brand">
      <div class="cover-brand-mark"></div>
      <div>
        <div class="cover-brand-name">Pelmar</div>
        <div class="cover-brand-sub">CAPITAL WEALTH</div>
      </div>
    </div>
  </section>

  <section class="slide" style="left:327px;top:47px">
    <div class="slide-title">OUR BELIEFS</div>
    <div class="beliefs-band"></div>
    <div class="belief" style="left:22px;top:36px">
      <svg class="belief-icon" style="left:0;top:0" viewBox="0 0 10 10"><text x="2" y="9" font-size="10" font-weight="700" fill="#123f84">$</text></svg>
      <div style="margin-left:16px"><div class="item-head">Cost Matters</div><p class="fine">We believe managing costs with care is key to strong returns. Fees compound over time, so we keep them low for our clients.</p></div>
    </div>
    <div class="belief" style="left:132px;top:36px">
      <svg class="belief-icon" style="left:0;top:0" viewBox="0 0 10 10"><path d="M0 2h4l1 1h5v6H0z" fill="#123f84"/></svg>
      <div style="margin-left:16px"><div class="item-head">Research Matters</div><p class="fine">We believe thorough research builds better portfolios. Our team studies each holding and the wider market with discipline.</p></div>
    </div>
    <div class="belief" style="left:22px;top:80px">
      <svg class="belief-icon" style="left:0;top:0" viewBox="0 0 10 10"><circle cx="4" cy="4" r="3" fill="none" stroke="#123f84" stroke-width="1.2"/><path d="M6 6l3.5 3.5" stroke="#123f84" stroke-width="1.4"/></svg>
      <div style="margin-left:16px"><div class="item-head">Focus Matters</div><p class="fine">We believe a focused plan serves clients best. We hold a clear set of goals and avoid noise that distracts from them.</p></div>
    </div>
    <div class="belief" style="left:132px;top:80px">
      <svg class="belief-icon" style="left:0;top:0" viewBox="0 0 10 10"><circle cx="5" cy="3" r="2.2" fill="none" stroke="#123f84" stroke-width="1.2"/><path d="M5 5v5M5 8h2" stroke="#123f84" stroke-width="1.2"/></svg>
      <div style="margin-left:16px"><div class="item-head">Access Matters</div><p class="fine">We believe clients deserve direct access to their advisors and clear reporting whenever questions arise.</p></div>
    </div>
    <div class="slide-footer"></div><div class="slide-footer-mark"></div>
  </section>

  <section class="slide" style="left:601px;top:47px">
    <div class="slide-title">THE PELMAR DIFFERENCE</div>
    <div class="diff-cell" style="left:12px;top:34px"><div class="item-head">Experience</div><p class="fine">Our team brings decades of market work to every client plan and every portfolio decision we make together.</p></div>
    <div class="diff-cell" style="left:90px;top:34px"><div class="item-head">Independence</div><p class="fine">We are owned by our staff and answer only to clients, free from sales targets or outside product ties.</p></div>
    <div class="diff-cell" style="left:168px;top:34px"><div class="item-head">Accountability</div><p class="fine">We own our results and report them plainly, so clients always know how their money is doing.</p></div>
    <div class="diff-cell" style="left:12px;top:80px"><div class="item-head">Alignment</div><p class="fine">We invest beside our clients, so our interests rise and fall with theirs over time.</p></div>
    <div class="diff-cell" style="left:90px;top:80px"><div class="item-head">Focus</div><p class="fine">We manage to our strengths and keep a tight set of strategies that we know well.</p></div>
    <div class="diff-cell" style="left:168px;top:80px"><div class="item-head">Transparency</div><p class="fine">We share fees, holdings and reasoning openly, so trust is earned and kept.</p></div>
    <div class="slide-footer"></div><div class="slide-footer-mark"></div>
  </section>

  <section class="slide" style="left:874px;top:47px">
    <div class="slide-title">EDIT TITLE HERE</div>
    <div class="lorem-box" style="left:20px;top:42px"><span class="lorem-box-tab"></span><div class="lorem-box-head">LOREM IPSUM</div><p class="fine">Short note text here</p></div>
    <div class="lorem-box" style="left:74px;top:42px"><span class="lorem-box-tab"></span><div class="lorem-box-head">LOREM IPSUM</div><p class="fine">Short note text here</p></div>
    <div class="lorem-box" style="left:128px;top:42px"><span class="lorem-box-tab"></span><div class="lorem-box-head">LOREM IPSUM</div><p class="fine">Short note text here</p></div>
    <div class="lorem-box" style="left:182px;top:42px"><span class="lorem-box-tab"></span><div class="lorem-box-head">LOREM IPSUM</div><p class="fine">Short note text here</p></div>
    <div class="lorem-box" style="left:20px;top:82px"><span class="lorem-box-tab"></span><div class="lorem-box-head">LOREM IPSUM</div><p class="fine">Short note text here</p></div>
    <div class="lorem-box" style="left:74px;top:82px"><span class="lorem-box-tab"></span><div class="lorem-box-head">LOREM IPSUM</div><p class="fine">Short note text here</p></div>
    <div class="lorem-box" style="left:128px;top:82px"><span class="lorem-box-tab"></span><div class="lorem-box-head">LOREM IPSUM</div><p class="fine">Short note text here</p></div>
    <div class="lorem-box" style="left:182px;top:82px"><span class="lorem-box-tab"></span><div class="lorem-box-head">LOREM IPSUM</div><p class="fine">Short note text here</p></div>
    <div class="slide-footer"></div><div class="slide-footer-mark"></div>
  </section>

  <!-- Row 2 -->
  <section class="slide" style="left:53px;top:213px">
    <div class="slide-title">EDIT TITLE HERE</div>
    <div class="abs" style="left:10px;top:24px;width:166px;height:72px;background:linear-gradient(180deg,#b4b6b8,#a3a5a8);border-radius:4px" role="img" aria-label="World map with office location pins"></div>
    <div class="legend" style="top:95px"><span class="legend-dot" style="background:var(--blue)"></span>EDIT TITLE HERE</div>
    <div class="legend" style="top:109px"><span class="legend-dot" style="background:#5a5d63"></span>EDIT TITLE HERE</div>
    <div class="slide-footer"></div><div class="slide-footer-mark"></div>
  </section>

  <section class="slide slide--navy" style="left:327px;top:213px">
    <svg class="abs" style="left:101px;top:28px" width="46" height="46" viewBox="0 0 46 46"><circle cx="23" cy="23" r="21" fill="none" stroke="#fff" stroke-width="1.6"/><text x="23" y="31" text-anchor="middle" font-family="Open Sans, sans-serif" font-size="22" fill="#fff">?</text></svg>
    <div class="thanks" style="top:88px;font-size:9px">QUESTIONS</div>
  </section>

  <section class="slide" style="left:601px;top:213px">
    <div class="slide-title">EDIT TITLE HERE</div>
    <p class="lead abs" style="left:14px;top:22px">Lorem ipsum dolor sit amet, consectetur adipiscing elit. Aenean sed tempor lorem.</p>
    <div class="photo photo--office" style="left:14px;top:32px;width:124px;height:56px" role="img" aria-label="Photo of a business team reviewing documents"></div>
    <div class="abs" style="left:138px;top:32px;width:96px;height:56px;background:var(--navy);padding:7px 6px">
      <div style="font-size:3.6px;font-weight:700;color:#fff;margin-bottom:2px">LOREM IPSUM</div>
      <p class="fine fine--white">Our advisors meet each client often to review goals, risk and progress with care.</p>
    </div>
    <p class="fine abs" style="left:14px;top:94px;width:220px">We build each plan around the client, with steady review and plain reporting. Our team studies markets daily and shares clear views on risk, cost and growth so clients can decide with confidence and calm.</p>
    <div class="slide-footer"></div><div class="slide-footer-mark"></div>
  </section>

  <section class="slide" style="left:874px;top:213px">
    <div class="slide-title">OUR BELIEFS</div>
    <div class="abs" style="left:0;top:24px;width:106px;height:104px;background:#f1f1f1"></div>
    <div class="num-row" style="top:31px"><b>01</b><span class="fine">Lorem ipsum dolor sit amet</span></div>
    <div class="num-row" style="top:46px"><b>02</b><span class="fine">Lorem ipsum dolor sit amet</span></div>
    <div class="num-row" style="top:61px"><b>03</b><span class="fine">Lorem ipsum dolor sit amet</span></div>
    <div class="num-row" style="top:76px"><b>04</b><span class="fine">Lorem ipsum dolor sit amet</span></div>
    <div class="num-row" style="top:91px"><b>05</b><span class="fine">Lorem ipsum dolor sit amet</span></div>
    <div class="num-row" style="top:106px"><b>06</b><span class="fine">Lorem ipsum dolor sit amet</span></div>
    <div class="photo photo--finance" style="left:106px;top:24px;width:142px;height:104px" role="img" aria-label="Photo of financial charts on a screen"></div>
    <div class="slide-footer"></div><div class="slide-footer-mark"></div>
  </section>

  <!-- Row 3 -->
  <section class="slide slide--navy" style="left:53px;top:375px">
    <svg class="abs" style="left:26px;top:90px" width="22" height="18" viewBox="0 0 22 18"><rect x="1" y="4" width="20" height="13" rx="2" fill="#fff"/><rect x="7" y="1" width="8" height="4" rx="1" fill="none" stroke="#fff" stroke-width="1.4"/><rect x="10" y="7" width="2" height="8" fill="#123f84"/></svg>
    <div class="abs" style="left:56px;top:88px;font-size:9px;font-weight:700;color:#fff">Section Title</div>
    <p class="fine fine--white abs" style="left:56px;top:101px;width:90px">Lorem ipsum dolor sit amet, consectetur adipiscing elit, sed do eiusmod.</p>
  </section>

  <section class="slide" style="left:327px;top:375px">
    <div class="slide-title">EDIT TITLE HERE</div>
    <p class="lead abs" style="left:14px;top:21px">Lorem ipsum dolor sit amet, consectetur adipiscing elit. Aenean sed tempor lorem.</p>
    <div class="photo photo--office" style="left:14px;top:30px;width:220px;height:44px" role="img" aria-label="Photo of a boardroom meeting"></div>
    <div class="tag" style="left:14px;background:var(--grey)">Lorem ipsum dolor</div>
    <div class="tag" style="left:71px;background:var(--navy)">Lorem ipsum dolor</div>
    <div class="tag" style="left:128px;background:var(--grey)">Lorem ipsum dolor</div>
    <div class="tag" style="left:185px;background:var(--navy)">Lorem ipsum dolor</div>
    <p class="fine abs" style="left:14px;top:94px;width:49px">Plans built with care and clear steps for each client goal.</p>
    <p class="fine abs" style="left:71px;top:94px;width:49px">Plans built with care and clear steps for each client goal.</p>
    <p class="fine abs" style="left:128px;top:94px;width:49px">Plans built with care and clear steps for each client goal.</p>
    <p class="fine abs" style="left:185px;top:94px;width:49px">Plans built with care and clear steps for each client goal.</p>
    <div class="slide-footer"></div><div class="slide-footer-mark"></div>
  </section>

  <section class="slide" style="left:601px;top:375px">
    <div class="slide-title">EDIT TITLE HERE</div>
    <div class="abs" style="left:8px;top:36px;width:92px;height:90px;background:var(--navy);padding:8px 7px">
      <p class="fine fine--white">We serve individuals and institutions with the same steady process, clear fees and direct access to the people who manage their money.</p>
      <p class="fine fine--white" style="margin-top:4px">Each portfolio is reviewed on a set schedule and adjusted only when the plan or the facts change.</p>
    </div>
    <div class="photo photo--office" style="left:100px;top:36px;width:140px;height:90px" role="img" aria-label="Photo of a team working at a desk with laptops and charts"></div>
  </section>

  <section class="slide" style="left:874px;top:375px">
    <div class="slide-title">EDIT TITLE HERE</div>
    <div class="member" style="left:24px"><div class="member-photo" role="img" aria-label="Portrait of Clara Hale"></div><div class="member-name">CLARA HALE</div><div class="member-role">General Manager</div></div>
    <div class="member" style="left:76px"><div class="member-photo" role="img" aria-label="Portrait of Owen Pike"></div><div class="member-name">OWEN PIKE</div><div class="member-role">Trainer Head</div></div>
    <div class="member" style="left:128px"><div class="member-photo" role="img" aria-label="Portrait of Lucas Reed"></div><div class="member-name">LUCAS REED</div><div class="member-role">Finance</div></div>
    <div class="member" style="left:180px"><div class="member-photo" role="img" aria-label="Portrait of Ivan Marsh"></div><div class="member-name">IVAN MARSH</div><div class="member-role">Senior Trainer</div></div>
    <p class="fine abs" style="left:22px;top:98px;width:204px">Our team works side by side with each client, bringing deep market knowledge, careful research and a shared focus on long term results and honest advice.</p>
    <div class="slide-footer"></div><div class="slide-footer-mark"></div>
  </section>

  <!-- Row 4 -->
  <section class="slide" style="left:53px;top:541px">
    <div class="slide-title">EDIT TITLE HERE</div>
    <div class="photo photo--city" style="left:20px;top:26px;width:228px;height:98px" role="img" aria-label="Photo of a city skyline at dusk with network lines"></div>
    <div class="abs" style="left:20px;top:26px;width:82px;height:98px;background:rgba(18,63,132,.88);padding:8px 7px">
      <div style="font-size:5px;font-weight:700;color:#fff;margin-bottom:3px">LOREM IPSUM</div>
      <p class="fine fine--white">We connect clients to markets with clear plans, steady review and honest reporting on every holding we manage for them.</p>
      <p class="fine fine--white" style="margin-top:3px">Our process is simple to follow and built to last through changing markets and seasons.</p>
    </div>
    <div class="slide-footer"></div><div class="slide-footer-mark"></div>
  </section>

  <section class="slide" style="left:327px;top:541px">
    <div class="slide-title">EDIT TITLE HERE</div>
    <div class="phone-copy" style="left:48px;top:34px"><b>Lorem ipsum dolor sit</b><p class="fine">Clear plans for every goal.</p></div>
    <div class="phone-copy" style="left:48px;top:62px"><b>Lorem ipsum dolor sit</b><p class="fine">Clear plans for every goal.</p></div>
    <div class="phone-copy" style="left:48px;top:96px"><b>Lorem ipsum dolor sit</b><p class="fine">Clear plans for every goal.</p></div>
    <svg class="abs" style="left:104px;top:34px" width="40" height="74" viewBox="0 0 40 74"><rect x="1" y="1" width="38" height="72" rx="4" fill="none" stroke="#123f84" stroke-width="2"/><rect x="5" y="9" width="30" height="52" fill="#bfc1c4"/><circle cx="20" cy="67" r="2.2" fill="#123f84"/></svg>
    <div class="phone-copy" style="left:162px;top:34px"><b>Lorem ipsum dolor sit</b><p class="fine">Clear plans for every goal.</p></div>
    <div class="phone-copy" style="left:162px;top:56px"><b>Lorem ipsum dolor sit</b><p class="fine">Clear plans for every goal.</p></div>
    <div class="phone-copy" style="left:162px;top:78px"><b>Lorem ipsum dolor sit</b><p class="fine">Clear plans for every goal.</p></div>
    <div class="phone-copy" style="left:162px;top:100px"><b>Lorem ipsum dolor sit</b><p class="fine">Clear plans for every goal.</p></div>
    <div class="slide-footer"></div><div class="slide-footer-mark"></div>
  </section>

  <section class="slide" style="left:601px;top:541px">
    <div class="photo photo--city" style="inset:0" role="img" aria-label="Photo of a city at night with light trails"></div>
    <div class="abs" style="left:32px;top:0;width:80px;height:140px;background:rgba(18,63,132,.82);padding:38px 7px 0">
      <div style="font-size:8px;font-weight:700;color:#fff;margin-bottom:3px">Section Title</div>
      <p class="fine fine--white">Lorem ipsum dolor sit amet, consectetur adipiscing elit. Curabitur nisl justo, ultrices eu consequat, condimentum in magna.</p>
    </div>
  </section>

  <section class="slide" style="left:874px;top:541px">
    <div class="slide-title">EDIT TITLE HERE</div>
    <div class="icon-dot" style="left:26px;top:32px"><svg viewBox="0 0 10 10"><path d="M1 4L5 1l4 3zM2 5h1v4H2zm2.5 0h1v4h-1zM7 5h1v4H7z" fill="#fff"/></svg></div>
    <div class="icon-dot" style="left:26px;top:55px"><svg viewBox="0 0 10 10"><circle cx="3" cy="3.5" r="1.6" fill="#fff"/><circle cx="7" cy="3.5" r="1.6" fill="#fff"/><path d="M0 9c0-2 1.5-3 3-3s3 1 3 3zM4 9c0-2 1.5-3 3-3s3 1 3 3z" fill="#fff"/></svg></div>
    <div class="icon-dot" style="left:26px;top:78px"><svg viewBox="0 0 10 10"><path d="M1 6l1.5-3h5L9 6v2H1z" fill="#fff"/></svg></div>
    <div class="icon-dot" style="left:26px;top:101px"><svg viewBox="0 0 10 10"><rect x="1" y="3" width="8" height="6" fill="#fff"/><rect x="3.5" y="1" width="3" height="2.5" fill="none" stroke="#fff"/></svg></div>
    <div class="abs" style="left:40px;top:32px;width:70px"><p class="fine" style="font-weight:700">Lorem ipsum dolor</p><p class="fine">A steady plan for each client.</p></div>
    <div class="abs" style="left:40px;top:55px;width:70px"><p class="fine" style="font-weight:700">Lorem ipsum dolor</p><p class="fine">A steady plan for each client.</p></div>
    <div class="abs" style="left:40px;top:78px;width:70px"><p class="fine" style="font-weight:700">Lorem ipsum dolor</p><p class="fine">A steady plan for each client.</p></div>
    <div class="abs" style="left:40px;top:101px;width:70px"><p class="fine" style="font-weight:700">Lorem ipsum dolor</p><p class="fine">A steady plan for each client.</p></div>
    <div class="photo photo--office" style="left:133px;top:0;width:115px;height:140px" role="img" aria-label="Photo of colleagues talking in a bright office"></div>
    <div class="slide-footer" style="right:120px"></div><div class="slide-footer-mark"></div>
  </section>

  <!-- Row 5 -->
  <section class="slide" style="left:327px;top:707px">
    <div class="slide-title">EDIT TITLE HERE</div>
    <p class="fine abs" style="left:40px;top:28px;width:196px">We guide clients with clear plans and honest advice. Each portfolio is built with care, reviewed often and reported in plain words so every client knows where they stand.</p>
    <div class="abs" style="left:0;top:44px;width:248px;height:72px;background:var(--navy)"></div>
    <svg class="abs" style="left:12px;top:34px" width="62" height="58" viewBox="0 0 62 58"><rect x="1" y="1" width="60" height="40" rx="2" fill="#dcdfe3" stroke="#8a8e93"/><rect x="4" y="4" width="54" height="34" fill="#f4f5f6"/><path d="M26 41h10l2 10H24z" fill="#b7bbc0"/><rect x="18" y="51" width="26" height="3" rx="1" fill="#c9ccd0"/></svg>
    <div class="icon-dot" style="left:96px;top:62px;width:11px;height:11px;background:#fff"><svg viewBox="0 0 10 10"><path d="M1 2h8v6H1z" fill="#123f84"/></svg></div>
    <div class="icon-dot" style="left:136px;top:62px;width:11px;height:11px;background:#fff"><svg viewBox="0 0 10 10"><path d="M2 8a2 2 0 010-4 3 3 0 016-1 2.5 2.5 0 010 5z" fill="#123f84"/></svg></div>
    <div class="icon-dot" style="left:176px;top:62px;width:11px;height:11px;background:#fff"><svg viewBox="0 0 10 10"><circle cx="5" cy="5" r="3" fill="none" stroke="#123f84" stroke-width="2" stroke-dasharray="2 1"/></svg></div>
    <div class="icon-dot" style="left:216px;top:62px;width:11px;height:11px;background:#fff"><svg viewBox="0 0 10 10"><rect x="4" y="0.5" width="2" height="2" fill="#123f84"/><rect x="0.5" y="7" width="2" height="2" fill="#123f84"/><rect x="4" y="7" width="2" height="2" fill="#123f84"/><rect x="7.5" y="7" width="2" height="2" fill="#123f84"/><path d="M5 2.5v4.5M1.5 7V5h7v2" stroke="#123f84" fill="none" stroke-width=".8"/></svg></div>
    <p class="fine fine--white abs" style="left:87px;top:77px;width:30px;text-align:center">Lorem ipsum dolor sit amet</p>
    <p class="fine fine--white abs" style="left:127px;top:77px;width:30px;text-align:center">Lorem ipsum dolor sit amet</p>
    <p class="fine fine--white abs" style="left:167px;top:77px;width:30px;text-align:center">Lorem ipsum dolor sit amet</p>
    <p class="fine fine--white abs" style="left:207px;top:77px;width:30px;text-align:center">Lorem ipsum dolor sit amet</p>
    <p class="fine abs" style="left:40px;top:119px;width:196px">Our process stays simple, clear and focused on client goals at every step.</p>
    <div class="slide-footer"></div><div class="slide-footer-mark"></div>
  </section>

  <section class="slide slide--navy" style="left:601px;top:707px">
    <div class="photo photo--office" style="inset:0;opacity:.5" role="img" aria-label="Photo of an empty boardroom with city windows"></div>
    <div class="abs" style="inset:0;background:rgba(18,63,132,.7)"></div>
    <div class="abs" style="left:58px;right:58px;top:48px;border-top:.8px solid rgba(255,255,255,.8)"></div>
    <div class="thanks" style="top:52px;font-size:19px;letter-spacing:.5px">THANK YOU</div>
    <div class="abs" style="left:58px;right:58px;top:79px;border-top:.8px solid rgba(255,255,255,.8)"></div>
    <div class="thanks" style="top:84px;font-size:4.5px">www.PelmarCW.com</div>
  </section>

</main>
</body>
</html>
```